New Invitation Design Project

We are looking for someone to design our e-vite, save the date and wine labels for our upcoming event on June 26th. Our event is an open house for our current clients and business colleagues to show our appreciation for them. We want to incorporate our new logo. We would like a professional but fun invitation with multiple versions in different manners of the design we choose.

Industry/Entity Type

House

```html
<!DOCTYPE html>
<html lang="en">
<head>
<meta charset="utf-8">
<title>HB&amp;K Open House Stationery</title>
<link href="https://fonts.googleapis.com/css2?family=Cinzel:wght@400;600&family=Questrial&family=Arimo&family=Crimson+Pro:ital,wght@0,400;1,700&display=swap" rel="stylesheet">
<style>
:root{
  --canvas:#ffffff;
  --card-black:#1b1b1b;
  --gold:#d4ab5e;
  --gold-light:#f0d08a;
  --gold-dark:#8a6424;
  --lime:#9fcc2e;
  --white:#ffffff;
  --slate:#4a5660;
}
*{margin:0;padding:0;box-sizing:border-box}
html,body{width:1200px;height:900px;overflow:hidden;background:var(--canvas)}
.canvas{position:relative;width:1200px;height:900px}
.card{position:absolute;background:var(--card-black);overflow:visible}

/* Save the date */
.save-date{left:392px;top:47px;width:416px;height:269px;overflow:hidden}
.gold-band{position:absolute;left:0;width:100%;height:11px;
  background:linear-gradient(90deg,var(--gold-dark),var(--gold-light) 40%,var(--gold) 70%,var(--gold-dark))}
.gold-band.top{top:0}
.gold-band.bottom{bottom:0}
.toast-photo{position:absolute;right:0;top:11px;width:190px;height:247px;
  background:linear-gradient(90deg,var(--card-black) 0%,#5a3f1e 35%,#a87a3c 70%,#c99a55 100%)}
.save-title{position:absolute;left:14px;top:28px;font-family:"Cinzel",serif;font-weight:600;
  color:var(--gold);font-size:26px;line-height:1}
.save-sub{position:absolute;left:14px;top:56px;font-family:"Cinzel",serif;color:var(--gold);font-size:19px}
.save-body{position:absolute;left:15px;top:107px;font-family:"Questrial",sans-serif;
  color:var(--gold-light);font-size:12.5px;line-height:16.3px;font-weight:700}
.save-firm{position:absolute;left:15px;top:213px;font-family:"Cinzel",serif;color:var(--gold);
  font-size:10.5px;line-height:13.5px}
.save-web{position:absolute;right:24px;top:239px;font-family:"Cinzel",serif;color:var(--gold);
  font-size:10px;letter-spacing:1px;text-transform:lowercase}

/* Shared photo header & contact block */
.photo{position:absolute;left:0;top:0;width:100%}
.contact{position:absolute;left:18px;top:168px;font-family:"Arimo",sans-serif;color:var(--lime);
  font-size:9.6px;line-height:10.8px}

/* Invitation front */
.invite{left:193px;top:595px;width:386px;height:257px}
.invite .photo{height:150px;background:linear-gradient(180deg,#5a5e62,#3e4448 60%,#2e3236)}
.invite-head{position:absolute;left:0;width:100%;top:44px;text-align:center;color:var(--white);
  font-family:"Crimson Pro",serif;font-size:23px;line-height:27px}
.invite-head em{font-style:italic;font-weight:700}
.tab{position:absolute}

/* Invitation inside */
.details{left:621px;top:446px;width:385px;height:406px}
.details .photo{height:149px;background:linear-gradient(180deg,#56626b,#46525b)}
.details-text{position:absolute;left:0;width:100%;top:182px;text-align:center;color:var(--white);
  font-family:"Crimson Pro",serif;font-size:22px;line-height:26px}
.details .contact{top:316px}
</style>
</head>
<body>
<div class="canvas">

  <section class="card save-date">
    <div class="gold-band top"></div>
    <div class="toast-photo" role="img" aria-label="Photo of hands raising champagne glasses in a toast"></div>
    <h1 class="save-title">SAVE THE DATE</h1>
    <p class="save-sub">June 26, 2014</p>
    <p class="save-body">Please join us for our<br>Open House Celebration<br>Thursday, June 26, 2014<br>3:00 to 7:00 PM</p>
    <p class="save-firm">HB&amp;K<br>Hale, Brenner &amp; Koss<br>555-014-2270</p>
    <p class="save-web">www.hbklegal.com</p>
    <div class="gold-band bottom"></div>
  </section>

  <section class="card invite">
    <div class="photo" role="img" aria-label="Photo of guests at a table raising wine glasses"></div>
    <h2 class="invite-head"><em>You're Invited to</em><br>the HBK Open House!</h2>
    <svg class="tab" style="left:174px;top:140px" width="40" height="20" viewBox="0 0 40 20" aria-hidden="true">
      <path d="M0 10 H6 A14 10 0 0 0 34 10 H40" fill="none" stroke="#777" stroke-width="1"/>
      <path d="M6 10 A14 10 0 0 0 34 10 Z" fill="#555a5e"/>
    </svg>
    <p class="contact">1420 Birchmont Avenue, Suite 210, Lakeview Park, IL 60099<br>HB&amp;K<br>Hale, Brenner &amp; Koss<br>Attorneys at Law<br>555-014-2270<br>www. hbklegal.com<br>RSVP to mreyes@hbklegal.com or (555) 014-2270</p>
  </section>

  <section class="card details">
    <svg class="tab" style="left:174px;top:-12px" width="36" height="14" viewBox="0 0 36 14" aria-hidden="true">
      <path d="M1 14 A17 13 0 0 1 35 14 Z" fill="#8a8f93" stroke="#666" stroke-width="1"/>
    </svg>
    <div class="photo" role="img" aria-label="Portrait photo of three attorneys in dark suits"></div>
    <p class="details-text">Thursday, June 26, 2014<br>3:00pm - 7:00pm<br>Drop by any time!</p>
    <p class="contact">1420 Birchmont Avenue, Suite 210, Lakeview Park, IL 60099<br>HB&amp;K<br>Hale, Brenner &amp; Koss<br>Attorneys at Law<br>555-014-2270<br>www. hbklegal.com<br>RSVP to mreyes@hbklegal.com or (555) 014-2270</p>
  </section>

</div>
</body>
</html>
```